Automotive component supplier needs a business card design

We need a business card design for our company called Vexlo Global Fittings Ltd based in the UK. We are a supplier of interior and exterior components to premium car manufacturers such as Harwick Vale, Denby Stroud, Calloway and Ferrucatti. We would like to see a modern business card design that uses the colour blue.

Target Market(s)

Premium automotive car manufacturers.

Industry/Entity Type

Automotive

Contact Information for Business Card

Company Name : Vexlo Global Fittings Limited
Address: 17 Tamsin Yard, Upper Heath, Warwick, CV32 8LN, United Kingdom
Web Address : www.vexlofittings-demo.co.uk

Font styles to use
Other font styles liked:
• Helvetica

Colors
3176b5
0255a3
85acd3
cfdeed
cee9f5
85cae6
34a6d7
0692cd
9bcb3c

Requirements
Must have
• Clear company logo and a mixture of blue colours.
Nice to have
• A high quality modern image.
Should not have
• Multiple colours.

```html
<!DOCTYPE html>
<html lang="en">
<head>
<meta charset="utf-8">
<title>Vexlo Global Fittings – Business Card</title>
<link href="https://fonts.googleapis.com/css2?family=Lato:wght@400;700&display=swap" rel="stylesheet">
<style>
  :root {
    --blue-main: #0a8fd2;
    --blue-deep: #0672b0;
    --accent-green: #9bcb3c;
    --ink: #2a2a2a;
    --paper: #ffffff;
    --backdrop: #e6e8eb;
  }
  * { margin: 0; padding: 0; box-sizing: border-box; }
  html, body { width: 1200px; height: 800px; overflow: hidden; }
  body {
    background: var(--backdrop);
    font-family: "Lato", Helvetica, Arial, sans-serif;
    position: relative;
  }
  .card {
    position: absolute;
    width: 540px;
    height: 310px;
    border-radius: 3px;
    box-shadow: 0 10px 28px rgba(0,0,0,0.18);
    overflow: hidden;
  }
  /* Front */
  .card--front {
    left: 40px; top: 245px;
    background: var(--blue-main);
    color: var(--paper);
  }
  .front-brand {
    position: absolute;
    left: 0; right: 0; top: 100px;
    display: flex; align-items: center; justify-content: center; gap: 14px;
  }
  .brand-mark {
    width: 16px; height: 16px;
    background: var(--accent-green);
    border-radius: 2px;
  }
  .brand-name {
    font-weight: 700;
    font-size: 38px;
    letter-spacing: 1px;
    text-transform: uppercase;
  }
  .front-web {
    position: absolute;
    left: 0; right: 0; bottom: 38px;
    text-align: center;
    font-size: 15px;
    letter-spacing: 2px;
  }
  /* Back */
  .card--back {
    left: 620px; top: 245px;
    background: var(--paper);
    border-bottom: 8px solid var(--blue-main);
  }
  .back-brand {
    position: absolute;
    left: 40px; top: 40px;
    display: flex; align-items: center; gap: 10px;
    color: var(--blue-main);
  }
  .back-brand .brand-name { font-size: 27px; }
  .back-brand .brand-mark { width: 12px; height: 12px; }
  .address {
    position: absolute;
    left: 40px; top: 118px;
    font-size: 14.5px;
    line-height: 1.35;
    color: var(--ink);
  }
  .contact-list {
    position: absolute;
    left: 40px; top: 192px;
    list-style: none;
    font-size: 14.5px;
    color: var(--ink);
  }
  .contact-list li {
    display: flex; align-items: center; gap: 12px;
    line-height: 1.45;
  }
  .contact-list svg { width: 13px; height: 13px; fill: var(--blue-main); flex: none; }
  .person {
    position: absolute;
    right: 40px; top: 110px;
    text-align: left;
  }
  .person-name {
    font-weight: 700;
    font-size: 22px;
    color: var(--blue-main);
  }
  .person-role {
    font-size: 14px;
    color: var(--ink);
    margin-top: 2px;
  }
</style>
</head>
<body>

<section class="card card--front">
  <div class="front-brand">
    <span class="brand-mark"></span>
    <span class="brand-name">Vexlo Global Fittings</span>
  </div>
  <p class="front-web">www.vexlofittings-demo.co.uk</p>
</section>

<section class="card card--back">
  <div class="back-brand">
    <span class="brand-mark"></span>
    <span class="brand-name">Vexlo Global Fittings</span>
  </div>

  <address class="address" style="font-style:normal">
    17 Tamsin Yard, Upper Heath<br>
    Warwick, CV32 8LN<br>
    United Kingdom
  </address>

  <ul class="contact-list">
    <li>
      <svg viewBox="0 0 16 16" aria-hidden="true"><path d="M3.6 1.2l2.2 2.6c.3.4.3.9 0 1.3L4.7 6.3c.9 2 2.6 3.7 4.9 4.9l1.2-1.1c.4-.3.9-.3 1.3 0l2.6 2.2c.4.4.4 1 0 1.4l-1.3 1.2C11.8 16.1 0 8.4 1.1 2.5L2.2 1.2c.4-.4 1-.4 1.4 0z"/></svg>
      512 004 2290
    </li>
    <li>
      <svg viewBox="0 0 16 16" aria-hidden="true"><path d="M4.5 0h7c.8 0 1.5.7 1.5 1.5v13c0 .8-.7 1.5-1.5 1.5h-7C3.7 16 3 15.3 3 14.5v-13C3 .7 3.7 0 4.5 0zM5 2v10h6V2H5zm3 11a1 1 0 100 2 1 1 0 000-2z"/></svg>
      512 004 2291
    </li>
    <li>
      <svg viewBox="0 0 16 16" aria-hidden="true"><path d="M0 3h16v10H0V3zm1.5 1.2v.3L8 9l6.5-4.5v-.3h-13zm0 1.8v5.8h13V6L8 10.5 1.5 6z"/></svg>
      info@vexlofittings-demo.co.uk
    </li>
    <li>
      <svg viewBox="0 0 16 16" aria-hidden="true"><path d="M8 0a8 8 0 100 16A8 8 0 008 0zm5.9 7.2h-2.5c-.1-1.9-.5-3.7-1.2-5a6.5 6.5 0 013.7 5zM8 1.6c.7.9 1.4 2.9 1.5 5.6h-3C6.6 4.5 7.3 2.5 8 1.6zM5.8 2.2c-.7 1.3-1.1 3.1-1.2 5H2.1a6.5 6.5 0 013.7-5zM2.1 8.8h2.5c.1 1.9.5 3.7 1.2 5a6.5 6.5 0 01-3.7-5zM8 14.4c-.7-.9-1.4-2.9-1.5-5.6h3c-.1 2.7-.8 4.7-1.5 5.6zm2.2-.6c.7-1.3 1.1-3.1 1.2-5h2.5a6.5 6.5 0 01-3.7 5z"/></svg>
      www.vexlofittings-demo.co.uk
    </li>
  </ul>

  <div class="person">
    <p class="person-name">Marcus Peller</p>
    <p class="person-role">Manager</p>
  </div>
</section>

</body>
</html>
```